LOLU Baby Massage Classes - flyer to make a difference

I need a single page flyer, preferably single page, to hand out to doctors, medical centres and parents. To also leave on counters of establishments.
It is to promote my baby massage classes. Mums can get together with other mums and book a 5 week course to learn and discover the many benefits of baby massage.
Benefits include: enhances bonding and attachment, understand non-verbal cues from your baby, helps with sleep patterns, help with immune system, increases vagal activity,relief from wind, colic or constipation to name some.

Baby age from birth to 12 months. Group classes or private sessions

I am a Professional Member and Certified by the Global Society of Newborn Touch (GSNT) GSNT Australia is Nationally Accredited and is endorsed by Crown Academy of Carers, the Southern Guild of Birth Attendants, The Southern Union of Daily Living Therapy Australia, The Southern Union of Bodywork Practitioner and is a full member of Wellmind Network Australia.

Class detail and availability contact is Petra Holm 0487 315 208 petra.joanne.holm@quillmail.example www.lolunewborntouch com.au facebook/comLOLUnewborntouch

My colour scheme is green and purple as you will see from my logo and website. I would like my flyer to be softer tones of either both colours or just one.

I will include some images you can choose from or show me any you think will fit in with baby massage. THANK YOU
Updates

Hi The size of my flyer is A6. Approx 150mms x 210mms and single sided. Thank you

Target Market(s)

mums and dads, groups, doctors, midwives

Industry/Entity Type

Medical

Font styles to use
Sans Serif

Colors
87d0c7
b09cc8

Requirements
Must have
• baby photo or photos, both my logo and the GSNT logo. The GSNT logo is to be small
• Baby Massage Classes (wording) is very important to catch the eye.
• Invitation to book a class or gather friends to book is next in importance
• Benefits is next
• The admin information ie.,membership, certification and endorsements are lesser and can be small.
• Contact information to be noticeable.
Nice to have
• If you have an idea, drawing or photo that would look better, please feel free to try it
Should not have
• should not be crowded with information all the same size

```html
<!DOCTYPE html>
<html lang="en">
<head>
<meta charset="utf-8">
<title>LOLU Baby Massage Classes – Flyer</title>
<link rel="stylesheet" href="https://fonts.googleapis.com/css2?family=Questrial&display=swap">
<style>
  :root {
    --teal: #87d0c7;
    --lilac: #b09cc8;
    --plum: #8b2c8c;
    --plum-deep: #6e2a8a;
    --ink: #111111;
    --white: #ffffff;
    --rule-grey: #5f5f5f;
    --skin-light: #efe4de;
    --skin-mid: #d9bfb2;
  }
  * { margin: 0; padding: 0; box-sizing: border-box; }
  html, body { width: 852px; height: 1200px; overflow: hidden; background: var(--teal); }
  body { font-family: "Questrial", "Century Gothic", sans-serif; color: var(--ink); }

  .flyer { position: relative; width: 852px; height: 1200px; background: var(--teal); overflow: hidden; }
  .flyer-shapes { position: absolute; inset: 0; width: 852px; height: 1200px; }

  .brand-mark {
    position: absolute; display: flex; align-items: center; justify-content: center;
    color: var(--plum); letter-spacing: 2px;
  }
  .brand-mark--society { left: 383px; top: -87px; width: 314px; height: 314px; font-size: 64px; padding-top: 60px; }
  .brand-mark--classes { left: 693px; top: 149px; width: 172px; height: 172px; font-size: 34px; color: var(--plum-deep); }

  .tagline-bar {
    position: absolute; left: 434px; top: 385px; width: 392px; height: 40px;
    background: var(--white); font-size: 25px; line-height: 40px; text-align: center; white-space: nowrap;
  }

  .main-copy { position: absolute; left: 298px; top: 494px; width: 520px; }
  .main-copy__title { font-size: 38px; font-weight: 400; line-height: 1.2; letter-spacing: 0; white-space: nowrap; }
  .main-copy__body { margin-top: 24px; font-size: 24px; line-height: 33px; }

  .info-card { position: absolute; left: 63px; width: 172px; background: var(--white); }
  .info-card__title {
    background: var(--lilac); height: 31px; font-size: 19px; font-weight: 400;
    line-height: 31px; text-align: center; color: var(--ink);
  }
  .info-card__text { padding: 7px 8px; font-size: 8.2px; line-height: 11.2px; overflow-wrap: anywhere; }
  .info-card--first { top: 530px; height: 175px; }
  .info-card--second { top: 708px; height: 168px; }
  .info-card--third { top: 885px; height: 168px; }

  .contact-disc {
    position: absolute; left: 423px; top: 1090px; width: 408px; text-align: center;
    font-size: 30px; line-height: 42px; font-style: normal;
  }
</style>
</head>
<body>
<main class="flyer">
  <svg class="flyer-shapes" viewBox="0 0 852 1200">
    <defs>
      <linearGradient id="photo-tone" x1="0" y1="0" x2="1" y2="1">
        <stop offset="0" stop-color="var(--skin-light)"/>
        <stop offset="1" stop-color="var(--skin-mid)"/>
      </linearGradient>
    </defs>
    <path d="M0,360 C170,385 320,345 405,288 C340,390 190,470 0,478 Z" fill="var(--lilac)"/>
    <path role="img" aria-label="Photo of a smiling baby lying down while a parent's hands massage its tummy"
          d="M0,0 H352 V160 C350,300 230,395 0,405 Z" fill="url(#photo-tone)"/>
    <path d="M352,160 C350,300 230,395 0,405" fill="none" stroke="var(--rule-grey)" stroke-width="6"/>
    <circle cx="540" cy="70" r="149" fill="var(--white)" stroke="var(--plum)" stroke-width="16"/>
    <circle cx="779" cy="235" r="80" fill="var(--white)" stroke="var(--plum)" stroke-width="12"/>
    <circle cx="736" cy="1240" r="290" fill="var(--lilac)"/>
    <circle cx="627" cy="1255" r="208" fill="var(--white)" stroke="var(--rule-grey)" stroke-width="7"/>
  </svg>

  <div class="brand-mark brand-mark--society">GSNT</div>
  <div class="brand-mark brand-mark--classes">LOLU</div>

  <div class="tagline-bar">LOLU Baby Massage Classes</div>

  <section class="main-copy">
    <h1 class="main-copy__title">BABY MASSAGE CLASSES</h1>
    <p class="main-copy__body">Gather your friends or join other mums and book a 5 week course. Discover the many benefits of baby massage for your little one, from birth to 12 months. Massage enhances bonding and attachment, helps you understand your baby's non-verbal cues and supports better sleep patterns. It helps the immune system, increases vagal activity and brings relief from wind, colic or constipation.</p>
  </section>

  <aside class="info-card info-card--first">
    <h2 class="info-card__title">BENEFITS</h2>
    <p class="info-card__text">Enhances bonding and attachment. Understand non-verbal cues from your baby. Helps with sleep patterns. Helps the immune system. Increases vagal activity. Relief from wind, colic or constipation. Gentle, calm time together for parent and baby in a warm and friendly setting.</p>
  </aside>
  <aside class="info-card info-card--second">
    <h2 class="info-card__title">BOOK A CLASS</h2>
    <p class="info-card__text">Group classes or private sessions for babies from birth to 12 months. For class details and availability contact Petra Holm on 0487 315 208.<br>petra.joanne.holm@quillmail.example<br>www.lolunewborntouch com.au<br>facebook/comLOLUnewborntouch</p>
  </aside>
  <aside class="info-card info-card--third">
    <h2 class="info-card__title">ACCREDITED</h2>
    <p class="info-card__text">Professional Member and Certified by the Global Society of Newborn Touch (GSNT). GSNT Australia is Nationally Accredited and endorsed by Crown Academy of Carers, the Southern Guild of Birth Attendants, The Southern Union of Daily Living Therapy Australia, The Southern Union of Bodywork Practitioner and is a full member of Wellmind Network Australia.</p>
  </aside>

  <address class="contact-disc">
    Petra Holm<br>0487 315 208
  </address>
</main>
</body>
</html>
```